brisknest

i want to ues this logo and the same colors used on the business card

cleaning & service

Industry/Entity Type

Business

Contact Information for Business Card

Font styles to use
Serif
Sans Serif
Decorative
Script

Colors
add136
0692cd
000000
5c5c5c
fbfbfb

Requirements
Must have
• cleaning things

```html
<!DOCTYPE html>
<html lang="en">
<head>
<meta charset="utf-8">
<title>brisknest business card</title>
<link rel="stylesheet" href="https://fonts.googleapis.com/css2?family=Work+Sans:wght@400;600&display=swap">
<style>
  :root {
    --green: #add136;
    --blue: #0692cd;
    --blue-deep: #0a63a8;
    --ink: #5c5c5c;
    --paper: #fbfbfb;
    --stage: #1b1b1d;
  }
  * { margin: 0; padding: 0; box-sizing: border-box; }
  html, body { width: 1200px; height: 963px; overflow: hidden; }
  body {
    background: var(--stage);
    font-family: "Work Sans", Arial, sans-serif;
    position: relative;
  }
  .card {
    position: absolute;
    left: 250px;
    width: 700px;
    height: 400px;
    border-radius: 18px;
    overflow: hidden;
  }
  .card-front { top: 60px; background: var(--paper); }
  .card-back {
    top: 503px;
    background: linear-gradient(135deg, var(--blue-deep) 0%, #1576bd 55%, #1a7fc4 100%);
    display: flex;
    align-items: center;
    justify-content: center;
  }
  .front-band {
    position: absolute; left: 0; right: 0; bottom: 0; height: 24px;
    background: var(--blue-deep);
  }
  .front-rule {
    position: absolute; left: 0; right: 0; bottom: 27px; height: 3px;
    background: var(--green);
  }
  .brand {
    display: flex; align-items: center; gap: 10px;
    font-weight: 600; letter-spacing: 0.5px;
  }
  .brand-dot { border-radius: 50%; flex: none; }
  .front-brand {
    position: absolute; left: 55px; top: 165px;
    color: var(--blue-deep); font-size: 32px;
  }
  .front-brand .brand-dot { width: 16px; height: 16px; background: var(--green); }
  .back-brand { color: var(--paper); font-size: 58px; }
  .back-brand .brand-dot { width: 26px; height: 26px; background: var(--paper); }
  .divider {
    position: absolute; left: 318px; top: 78px; width: 2px; height: 220px;
    background: var(--blue);
  }
  .details { position: absolute; left: 350px; top: 82px; color: var(--ink); }
  .name {
    color: var(--blue-deep); font-weight: 600; font-size: 30px;
    letter-spacing: 1px; line-height: 1.1;
  }
  .role { font-size: 16px; margin-top: 4px; }
  .address { font-size: 16px; line-height: 1.35; margin-top: 16px; }
  .contacts { list-style: none; margin-top: 14px; font-size: 16px; line-height: 1.45; }
  .contacts li { display: flex; align-items: center; gap: 10px; }
  .contacts svg { width: 13px; height: 13px; flex: none; }
</style>
</head>
<body>
  <section class="card card-front">
    <div class="brand front-brand"><span class="brand-dot"></span>brisknest</div>
    <div class="divider"></div>
    <div class="details">
      <p class="name">MARLA FINCH</p>
      <p class="role">Director</p>
      <p class="address">47 Alder Crescent,<br>Halton ON L7A 2K4</p>
      <ul class="contacts">
        <li>
          <svg viewBox="0 0 16 16" aria-hidden="true"><path fill="#0a63a8" d="M3.5 1.5l2.5 0 1 3.5-1.6 1.2a9 9 0 0 0 4.4 4.4L11 9l3.5 1v2.5c0 1-1 2-2 2A11 11 0 0 1 1.5 3.5c0-1 1-2 2-2z"/></svg>
          +330 5187-2294
        </li>
        <li>
          <svg viewBox="0 0 16 16" aria-hidden="true"><rect x="1.5" y="3.5" width="13" height="9" rx="1" fill="none" stroke="#0a63a8" stroke-width="1.6"/><path d="M2 4l6 5 6-5" fill="none" stroke="#0a63a8" stroke-width="1.6"/></svg>
          info@brisknest.com
        </li>
        <li>
          <svg viewBox="0 0 16 16" aria-hidden="true"><circle cx="8" cy="8" r="6.3" fill="none" stroke="#0a63a8" stroke-width="1.5"/><ellipse cx="8" cy="8" rx="2.8" ry="6.3" fill="none" stroke="#0a63a8" stroke-width="1.2"/><path d="M1.8 8h12.4" stroke="#0a63a8" stroke-width="1.2"/></svg>
          www.brisknest.com
        </li>
      </ul>
    </div>
    <div class="front-rule"></div>
    <div class="front-band"></div>
  </section>

  <section class="card card-back">
    <div class="brand back-brand"><span class="brand-dot"></span>brisknest</div>
  </section>
</body>
</html>
```